"Vows and Farewells by Meg" Web Site

I would like a web site designed for my funeral and wedding celebrancy business. My logo was designed by Artboard Hive (attached). I have written content of the web pages for reference (attached). I have attached logos designed through artboard hive and photos.
I am sure what else to write in a project description and would welcome suggestions

Target Market(s)

for marriages - brides and grooms, for funerals - families who have lost a loved one

Industry/Entity Type

Wedding Planner

Number of Pages Required

4 page

Font styles to use
Sans Serif

Colors
886aae
3277b5
33a6d7
a64599
e34096

Requirements
Must have
• a call to action (contact me) throughout
Nice to have
• nil
Should not have
• no morbid images

```html
<!DOCTYPE html>
<html lang="en">
<head>
<meta charset="utf-8">
<title>Vows and Farewells by Meg</title>
<link rel="stylesheet" href="https://fonts.googleapis.com/css2?family=Mulish:wght@400;600;700&family=Noto+Serif:wght@400&display=swap">
<style>
:root{
  --purple:#7e5ca8;
  --purple-soft:#9b80c2;
  --purple-pale:#c9b8de;
  --brand:#4d2f86;
  --ink:#555555;
  --ink-dark:#3d3d3d;
  --white:#ffffff;
  --footer:#353535;
}
*{box-sizing:border-box;margin:0;padding:0}
html,body{width:1200px;height:3719px;overflow:hidden}
body{position:relative;font-family:"Mulish",sans-serif;color:var(--ink);background:var(--white)}
.abs{position:absolute}
.photo{display:block}
.heading{font-family:"Noto Serif",serif;font-weight:400;text-transform:uppercase;text-align:center;left:0;width:1200px;font-size:40px;letter-spacing:1px}
.heading--purple{color:var(--purple)}
.heading--light{color:var(--white)}
.flourish{left:510px;width:180px;height:14px}
.flourish line{stroke-width:1.5}

/* hero */
.hero{left:0;top:0;width:1200px;height:665px;
  background:
    radial-gradient(ellipse 230px 260px at 200px 330px,rgba(255,255,255,.95),rgba(240,242,230,.7) 45%,rgba(170,190,140,.35) 75%,transparent 100%),
    radial-gradient(ellipse 90px 70px at 120px 260px,rgba(150,185,110,.55),transparent),
    radial-gradient(ellipse 70px 60px at 300px 420px,rgba(220,190,200,.55),transparent),
    radial-gradient(ellipse 380px 520px at 820px 200px,rgba(255,255,255,.95),rgba(245,242,238,.6) 60%,transparent),
    radial-gradient(ellipse 160px 120px at 540px 420px,rgba(220,190,170,.5),transparent),
    linear-gradient(100deg,#b9b5aa 0%,#d4d0c7 35%,#e8e5e0 60%,#cfcbc4 85%,#b3aea6 100%)}
.nav{left:79px;top:40px;width:1042px;height:79px;border-radius:40px;background:rgba(255,255,255,.55);display:flex;justify-content:center;align-items:center;gap:40px}
.nav a{font-size:17px;color:#666;text-decoration:none;text-transform:uppercase}
.nav a.is-active{color:var(--purple)}
.brand{left:0;top:462px;width:1200px;text-align:center;font-family:"Noto Serif",serif;font-size:68px;line-height:90px;color:var(--brand)}

/* welcome */
.intro{left:150px;top:826px;width:900px;text-align:center;font-size:15px;line-height:24px}
.intro p+p{margin-top:12px}
.btn{background:var(--purple);color:var(--white);border-radius:22px;text-align:center;font-size:20px;text-transform:uppercase;font-weight:600;text-decoration:none}
.btn--contact{left:506px;top:961px;width:188px;height:44px;line-height:44px}
.service{width:300px;height:300px}
.service__ring{position:absolute;left:6px;top:0;width:288px;height:288px;border-radius:50%;border:2px solid var(--purple-soft);padding:6px}
.service__photo{width:100%;height:100%;border-radius:50%}
.service svg{position:absolute;left:0;top:212px}
.service__label{position:absolute;left:0;top:222px;width:300px;text-align:center;color:var(--white);font-weight:700;font-size:18px;text-transform:uppercase}

/* portfolio */
.portfolio{left:0;top:1458px;width:1200px;height:706px;
  background:
    repeating-linear-gradient(160deg,rgba(255,255,255,.05) 0 40px,rgba(0,0,0,.08) 40px 80px),
    linear-gradient(160deg,#4a3f39 0%,#3a322e 45%,#4b413b 70%,#2f2926 100%)}
.tile{width:335px;height:208px;overflow:hidden}
.tile__overlay{position:absolute;inset:0;background:rgba(90,80,80,.5)}
.tile__frame{position:absolute;left:8px;top:8px;right:8px;bottom:8px;border:2px solid var(--white)}
.tile__name{position:absolute;left:0;top:64px;width:100%;text-align:center;color:var(--white);font-size:26px;font-weight:600}
.tile__icon{position:absolute;left:151px;top:106px}

/* blog */
.post__img{width:478px;height:241px;border-radius:0 60px 0 60px}
.post__title{font-size:24px;line-height:33px;color:var(--ink-dark);width:490px;font-weight:400}
.post__date{display:flex;align-items:center;gap:14px;font-size:16px}
.post__text{font-size:15px;line-height:24px;width:490px}

/* contact */
.contact{left:0;top:2967px;width:1200px;height:479px;
  background:
    radial-gradient(ellipse 260px 200px at 1050px 300px,rgba(210,150,160,.55),transparent),
    radial-gradient(ellipse 220px 180px at 120px 120px,rgba(140,160,110,.45),transparent),
    radial-gradient(ellipse 200px 160px at 900px 80px,rgba(220,200,200,.35),transparent),
    linear-gradient(120deg,#4e5a48 0%,#5f5a55 40%,#6d5f62 70%,#5d5a55 100%)}
.field{background:rgba(255,255,255,.45);color:var(--white);font-size:15px;padding:9px 16px}
.btn--send{left:516px;top:3332px;width:166px;height:42px;line-height:42px}

/* footer */
.footer{left:0;top:3446px;width:1200px;height:218px;background:var(--footer)}
.footer__item{width:360px;text-align:center;color:var(--white);font-size:16px;line-height:24px}
.footer__icon{width:60px;height:60px;border-radius:50%;border:2px solid rgba(255,255,255,.6);margin:0 auto 22px;display:flex;align-items:center;justify-content:center}
.legal{left:0;top:3664px;width:1200px;height:55px;background:var(--purple);color:var(--white);text-align:center;line-height:55px;font-size:15px}
</style>
</head>
<body>

<header>
  <div class="abs hero" role="img" aria-label="Bride in a white dress holding a bouquet of white and green flowers"></div>
  <nav class="abs nav">
    <a class="is-active" href="#">Home</a>
    <a href="#">About</a>
    <a href="#">Marriages</a>
    <a href="#">Funerals</a>
    <a href="#">Other Ceremonies</a>
    <a href="#">Contact</a>
  </nav>
  <div class="abs brand">Vows and Farewells by Meg</div>
</header>

<section>
  <h1 class="abs heading heading--purple" style="top:718px">Welcome to Vows and Farewells by Meg</h1>
  <svg class="abs flourish" style="top:790px" viewBox="0 0 180 14"><line x1="10" y1="7" x2="82" y2="7" stroke="#c9b8de"/><circle cx="90" cy="7" r="4" fill="#c9b8de"/><line x1="98" y1="7" x2="170" y2="7" stroke="#c9b8de"/></svg>
  <div class="abs intro">
    <p>My name is Meg Halvorsen and I am the owner of this business. My mission is to work with you to create a marriage, funeral or celebration service that truly celebrates love and life in an authentic way. Your way!</p>
    <p>I am legally authorised by the Commonwealth Attorney General's department to perform marriages across Australia and have completed a certificate IV in Celebrancy which included Marriage celebrancy units and Funeral celebrancy units</p>
  </div>
  <a class="abs btn btn--contact" href="#">Contact Us</a>

  <div class="abs service" style="left:88px;top:1078px">
    <div class="service__ring"><div class="service__photo" role="img" aria-label="Bride and groom showered with confetti" style="background:radial-gradient(circle at 30% 55%,#efe9e4 0 18%,transparent 40%),radial-gradient(circle at 68% 45%,#2c2c30 0 25%,transparent 50%),linear-gradient(180deg,#cfcac2,#8d8680 60%,#4a4744)"></div></div>
    <svg width="300" height="50" viewBox="0 0 300 50"><polygon points="0,8 28,8 28,44 0,44 12,26" fill="#6a4a94"/><polygon points="300,8 272,8 272,44 300,44 288,26" fill="#6a4a94"/><rect x="18" y="0" width="264" height="44" fill="#8866b0"/></svg>
    <div class="service__label">Marriages</div>
  </div>
  <div class="abs service" style="left:447px;top:1078px">
    <div class="service__ring"><div class="service__photo" role="img" aria-label="Hand placing a red rose on a casket" style="background:radial-gradient(circle at 35% 40%,#b8202a 0 8%,transparent 16%),radial-gradient(ellipse at 50% 25%,#c8737d 0 20%,transparent 45%),linear-gradient(170deg,#6f8a5e 0%,#5a3528 45%,#3a2219 70%,#d9d4ce 100%)"></div></div>
    <svg width="300" height="50" viewBox="0 0 300 50"><polygon points="0,8 28,8 28,44 0,44 12,26" fill="#6a4a94"/><polygon points="300,8 272,8 272,44 300,44 288,26" fill="#6a4a94"/><rect x="18" y="0" width="264" height="44" fill="#8866b0"/></svg>
    <div class="service__label">Funerals</div>
  </div>
  <div class="abs service" style="left:812px;top:1078px">
    <div class="service__ring"><div class="service__photo" role="img" aria-label="Pink flowers and glasses on a seaside table" style="background:radial-gradient(ellipse at 45% 60%,#e26aa6 0 18%,transparent 38%),radial-gradient(ellipse at 80% 55%,#eef2f4 0 12%,transparent 28%),linear-gradient(180deg,#3f7fb8 0%,#2c5e8e 45%,#cf8fb4 70%,#ecebea 100%)"></div></div>
    <svg width="300" height="50" viewBox="0 0 300 50"><polygon points="0,8 28,8 28,44 0,44 12,26" fill="#6a4a94"/><polygon points="300,8 272,8 272,44 300,44 288,26" fill="#6a4a94"/><rect x="18" y="0" width="264" height="44" fill="#8866b0"/></svg>
    <div class="service__label">Other Ceremonies</div>
  </div>
</section>

<section>
  <div class="abs portfolio" role="img" aria-label="Dimmed background of a wedding setting"></div>
  <h2 class="abs heading heading--light" style="top:1519px">Work Portfolio</h2>
  <svg class="abs flourish" style="top:1587px" viewBox="0 0 180 14"><line x1="10" y1="7" x2="82" y2="7" stroke="rgba(255,255,255,.7)"/><circle cx="90" cy="7" r="4" fill="#fff"/><line x1="98" y1="7" x2="170" y2="7" stroke="rgba(255,255,255,.7)"/></svg>

  <div class="abs tile" style="left:77px;top:1634px;background:radial-gradient(ellipse at 50% 75%,#f4f6f0 0 20%,transparent 45%),radial-gradient(ellipse at 20% 40%,#ffffff 0 15%,transparent 35%),linear-gradient(180deg,#8aa06a 0%,#c7d2b4 40%,#6d8150 100%)" role="img" aria-label="Couple at a floral wedding arch"></div>
  <div class="abs tile" style="left:434px;top:1634px;background:radial-gradient(ellipse at 60% 55%,#ffffff 0 22%,#e9ede0 40%,transparent 60%),linear-gradient(135deg,#f2f2ef,#d5d9cc 60%,#aab49e)" role="img" aria-label="White calla lily bouquet"></div>
  <div class="abs tile" style="left:791px;top:1634px">
    <div style="width:100%;height:100%;background:radial-gradient(ellipse at 30% 60%,#8a7b70,transparent 50%),radial-gradient(ellipse at 75% 55%,#d8cfc6,transparent 50%),linear-gradient(180deg,#a99b8e,#6f6259)" role="img" aria-label="Family group photo at a ceremony"></div>
    <div class="tile__overlay"></div>
    <div class="tile__frame"></div>
    <div class="tile__name">Project Name</div>
    <svg class="tile__icon" width="32" height="32" viewBox="0 0 24 24" fill="none" stroke="#fff" stroke-width="2.4" stroke-linecap="round"><path d="M10 14a4 4 0 0 0 5.7 0l3-3a4 4 0 0 0-5.7-5.7l-1 1"/><path d="M14 10a4 4 0 0 0-5.7 0l-3 3a4 4 0 0 0 5.7 5.7l1-1"/></svg>
  </div>
  <div class="abs tile" style="left:77px;top:1864px;background:radial-gradient(ellipse at 30% 25%,#f0f0f2 0 14%,transparent 32%),linear-gradient(180deg,#a6a29c 0%,#c9ab88 40%,#b08e68 75%,#9a7a55 100%)" role="img" aria-label="Couple walking on a sandy beach"></div>
  <div class="abs tile" style="left:434px;top:1864px;background:radial-gradient(ellipse at 40% 65%,#e0559c 0 18%,transparent 38%),radial-gradient(ellipse at 75% 60%,#f2f4f6 0 10%,transparent 25%),linear-gradient(180deg,#3c79b0 0%,#2f628f 45%,#d37fae 70%,#ecebea 100%)" role="img" aria-label="Pink flowers and glasses on a seaside table"></div>
  <div class="abs tile" style="left:791px;top:1864px;background:radial-gradient(ellipse at 45% 22%,#e29aa5 0 22%,transparent 45%),linear-gradient(180deg,#8ea27c 0%,#7d4a33 40%,#5b2f1c 70%,#8a9a70 100%)" role="img" aria-label="Wooden casket with a floral arrangement"></div>
</section>

<section>
  <h2 class="abs heading heading--purple" style="top:2208px">Latest Blog</h2>
  <svg class="abs flourish" style="top:2278px" viewBox="0 0 180 14"><line x1="10" y1="7" x2="82" y2="7" stroke="#c9b8de"/><circle cx="90" cy="7" r="4" fill="#c9b8de"/><line x1="98" y1="7" x2="170" y2="7" stroke="#c9b8de"/></svg>

  <div class="abs post__img" style="left:77px;top:2345px;background:radial-gradient(ellipse at 65% 70%,#f4f1ea 0 18%,transparent 38%),radial-gradient(circle at 20% 30%,#f6eedd 0 10%,transparent 25%),linear-gradient(120deg,#bfa67a,#e4d6bb 55%,#cbb48c)" role="img" aria-label="Wedding cake with a bride and groom topper"></div>
  <h3 class="abs post__title" style="left:632px;top:2375px">Lorem Ipsum is simply dummy text of the printing and typesetting industry.</h3>
  <div class="abs post__date" style="left:632px;top:2456px">
    <svg width="18" height="18" viewBox="0 0 18 18"><rect x="1" y="3" width="16" height="14" rx="2" fill="#9b80c2"/><rect x="3" y="7" width="12" height="8" fill="#fff"/><rect x="4" y="0" width="2" height="5" fill="#9b80c2"/><rect x="12" y="0" width="2" height="5" fill="#9b80c2"/></svg>
    <span>20 MAR 2018</span>
  </div>
  <p class="abs post__text" style="left:632px;top:2488px">Lorem Ipsum is simply dummy text of the printing and typesetting industry. Lorem Ipsum has been the industry's standard dummy text ever since the 1500s, when an unknown printer took a galley.</p>

  <h3 class="abs post__title" style="left:77px;top:2675px">Lorem Ipsum is simply dummy text of the printing and typesetting industry.</h3>
  <div class="abs post__date" style="left:77px;top:2756px">
    <svg width="18" height="18" viewBox="0 0 18 18"><rect x="1" y="3" width="16" height="14" rx="2" fill="#9b80c2"/><rect x="3" y="7" width="12" height="8" fill="#fff"/><rect x="4" y="0" width="2" height="5" fill="#9b80c2"/><rect x="12" y="0" width="2" height="5" fill="#9b80c2"/></svg>
    <span>20 MAR 2018</span>
  </div>
  <p class="abs post__text" style="left:77px;top:2788px">Lorem Ipsum is simply dummy text of the printing and typesetting industry. Lorem Ipsum has been the industry's standard dummy text ever since the 1500s, when an unknown printer took a galley.</p>
  <div class="abs post__img" style="left:645px;top:2648px;width:476px;height:238px;background:radial-gradient(ellipse at 20% 35%,#e7b2b8 0 12%,transparent 28%),radial-gradient(ellipse at 55% 65%,#f1c2c4 0 14%,transparent 30%),linear-gradient(120deg,#8e9f76,#ecebe6 45%,#e2e0da 70%,#b5c0a2)" role="img" aria-label="White chairs decorated with pink flowers"></div>
</section>

<section>
  <div class="abs contact" role="img" aria-label="Soft focus background of pink flowers"></div>
  <h2 class="abs heading heading--light" style="top:3026px">Contact Me</h2>
  <svg class="abs flourish" style="top:3095px" viewBox="0 0 180 14"><line x1="10" y1="7" x2="82" y2="7" stroke="rgba(255,255,255,.7)"/><circle cx="90" cy="7" r="4" fill="#fff"/><line x1="98" y1="7" x2="170" y2="7" stroke="rgba(255,255,255,.7)"/></svg>
  <div class="abs field" style="left:258px;top:3151px;width:332px;height:39px">Name</div>
  <div class="abs field" style="left:258px;top:3208px;width:332px;height:40px">Email</div>
  <div class="abs field" style="left:258px;top:3265px;width:332px;height:40px">Phone</div>
  <div class="abs field" style="left:607px;top:3151px;width:333px;height:154px">Message</div>
  <a class="abs btn btn--send" href="#">Send</a>
</section>

<footer>
  <div class="abs footer"></div>
  <div class="abs footer__item" style="left:70px;top:3495px">
    <div class="footer__icon"><svg width="22" height="22" viewBox="0 0 24 24" fill="none" stroke="#fff" stroke-width="1.8"><path d="M5 3h4l2 5-2.5 1.5a11 11 0 0 0 6 6L16 13l5 2v4a2 2 0 0 1-2 2A16 16 0 0 1 3 5a2 2 0 0 1 2-2z"/></svg></div>
    (+61) 0400 555 217
  </div>
  <div class="abs footer__item" style="left:420px;top:3495px">
    <div class="footer__icon"><svg width="22" height="22" viewBox="0 0 24 24" fill="none" stroke="#fff" stroke-width="1.8"><path d="M12 22s7-7 7-12a7 7 0 0 0-14 0c0 5 7 12 7 12z"/><circle cx="12" cy="10" r="2.5"/></svg></div>
    Meg Halvorsen P.O Box 812, Ridgevale<br>6099, Western Australia
  </div>
  <div class="abs footer__item" style="left:770px;top:3495px">
    <div class="footer__icon"><svg width="22" height="22" viewBox="0 0 24 24" fill="none" stroke="#fff" stroke-width="1.8"><rect x="3" y="5" width="18" height="14" rx="1"/><path d="M3 6l9 7 9-7"/></svg></div>
    meg@vowsandfarewells.example
  </div>
  <div class="abs legal">©Vows and Farewells by Meg. 2018 - All Rights Reserved.</div>
</footer>

</body>
</html>
```